BRV Company Introduction Presentation for Industrial Electronics and Automation

We are established since 2011 and we have 50 employees. We have two divisions in our company in Industrial Electronics Repair and Automation Solutions. We would like to make a presentation for those two sectors in our company.

BRV COMPANY provides Industrial Electronics Repairs and Supplies as well as Automation Solutions.
Industrial Electronics: We repair and supply all kind of Industrial Electronic equipment including: PLCs, Drives, Servo Drives, Invertor, HMIs, Controllers .. Etc.
Automation Solutions: Provide Automation Solutions & Services.

We have several presentations attached for your guideline and you can use the material and wording in needed.
We are present in 3 countries: Kuwait, Saudi, UAE with 5 offices. I have attached some material that can help in the presentation.
Our customers:
Factories: F&B, Steel, Packing, Paper, Chemical, Glass
Services Companies: O&M, Transport, Marine
Electricity – Water – Wastewater: DOH, NAR
Oil & Gas (Government & Private: GZLT, Vorba, PMA, HRB
Building Management Systems: Malls, Commercial Buildings, Stadium

What items do we repair & Supply?
Power Supplies, Secondary DC Supplies, Processor Cards, Memory Cards, Interface Modules, Analog I/O Cards, Digital I/O Cards, Communication Cards, Remote I/O, Distribution Panel, Program Loaders, PCB (Boards).
Operation Panels, Servo Drives, Servo Motors, Axis cards, Processor Cards, Memory Cards.
All Servo Drives & Motors, Transducers, Interface Cards.
Wire Feeders, Weld Timers.
Industrial Monitors, Message/Status Display, Operator Interfaces .
Robot Arms

What are the added values of brv?
QFP - QUALITY / Fast / Price

Target Market(s)

Industrial Factories, Energy, Water, Wastewater and Oil & Gas.

Colors
86cae7
0692cd

Requirements
Must have
• - Vission, mission, goal
- Our journey
- services
- clients (Kuwait & Saudi)
- Major brands,
- facility
- certification
- automation projects
- contact details for 3 countries
Nice to have
• other things
Should not have
• nothing in mind

```html
<!DOCTYPE html>
<html lang="en">
<head>
<meta charset="utf-8">
<title>BRV Company – Presentation Template</title>
<link href="https://fonts.googleapis.com/css2?family=Open+Sans:ital,wght@0,400;0,600;0,700;0,800;1,600&display=swap" rel="stylesheet">
<style>
:root{
  --blue:#0692cd;
  --sky:#86cae7;
  --deep:#0b5aa8;
  --navy:#0a3f7a;
  --ink:#1a2a3a;
  --grey:#7b8794;
  --canvas:#e4e7ea;
  --white:#ffffff;
  --panel:#f1f4f7;
}
*{margin:0;padding:0;box-sizing:border-box}
html,body{width:1200px;height:2784px;overflow:hidden;background:var(--canvas)}
body{font-family:"Open Sans",Arial,sans-serif;color:var(--ink);position:relative}
.slide{position:absolute;width:552px;height:310px;background:var(--white);overflow:hidden}
.col-l{left:42px}.col-r{left:607px}
.abs{position:absolute}
.brand{position:absolute;display:flex;align-items:center;gap:5px;font-weight:800;color:var(--blue);letter-spacing:2px}
.brand i{display:block;background:var(--blue)}
.brand.sm{top:10px;right:20px;font-size:14px}
.brand.sm i{width:11px;height:11px}
.slide-title{position:absolute;left:26px;top:20px;font-size:14px;font-weight:700;color:var(--deep);letter-spacing:-.2px}
.slide-title::before{content:"";position:absolute;left:-22px;top:5px;width:14px;height:2px;background:var(--blue);box-shadow:0 -4px 0 var(--blue),0 4px 0 var(--sky)}
.pgno{position:absolute;right:12px;bottom:10px;width:10px;height:10px;border:2px solid var(--blue);border-radius:50%}
.pgno::after{content:"";position:absolute;left:8px;top:2px;width:14px;height:2px;background:var(--blue)}
.ph{position:absolute}
.lorem{font-size:6px;line-height:1.45;color:var(--grey)}
.sub{font-size:9px;font-weight:600;color:var(--blue);letter-spacing:1.5px}
.white{color:var(--white)}
</style>
</head>
<body>

<!-- Row 1 -->
<section class="slide col-l" style="top:65px">
  <div class="brand sm" style="top:22px;right:28px;font-size:22px"><i style="width:18px;height:18px"></i>BRV</div>
  <div class="abs" style="left:0;top:80px;width:552px;height:170px;background:linear-gradient(90deg,var(--deep),var(--blue))"></div>
  <div class="ph" role="img" aria-label="Robotic hand reaching towards a glowing circuit line" style="left:200px;top:66px;width:352px;height:192px;background:radial-gradient(ellipse at 40% 55%,#e9eef3 0%,#b9c6d3 30%,rgba(6,146,205,0) 62%),linear-gradient(90deg,rgba(11,90,168,0),#46a8da 70%,#8fd0ec)"></div>
  <div class="abs white" style="left:26px;top:135px;font-size:19px;line-height:1.15;font-weight:400">A WORLD OF<br><span style="color:var(--sky);font-weight:700;letter-spacing:1px">SOLUTIONS</span></div>
</section>

<section class="slide col-r" style="top:65px">
  <div class="abs" role="img" aria-label="Blue globe network texture" style="left:0;top:0;width:166px;height:310px;background:radial-gradient(circle at 30% 30%,#2aa7e0,var(--blue) 50%,#0a7cc0)"></div>
  <div class="abs white" style="left:36px;top:140px;font-size:19px;font-weight:700;letter-spacing:1.5px">AGENDA</div>
  <div class="brand sm"><i></i>BRV</div>
  <div class="abs" style="left:218px;top:72px;width:252px">
    <div style="display:flex;flex-direction:column;gap:17px">
      <div style="display:flex;gap:6px;align-items:center"><i style="width:20px;height:20px;background:var(--deep)"></i><span style="flex:1;background:var(--blue);color:#fff;font-size:9px;font-weight:700;padding:4px 7px;letter-spacing:.6px">OUR VISION, MISSION AND GOAL</span></div>
      <div style="display:flex;gap:6px;align-items:center"><i style="width:20px;height:20px;background:var(--deep)"></i><span style="flex:1;background:var(--blue);color:#fff;font-size:9px;font-weight:700;padding:4px 7px;letter-spacing:.6px">OUR JOURNEY</span></div>
      <div style="display:flex;gap:6px;align-items:center"><i style="width:20px;height:20px;background:var(--deep)"></i><span style="flex:1;background:var(--blue);color:#fff;font-size:9px;font-weight:700;padding:4px 7px;letter-spacing:.6px">OUR SERVICES</span></div>
      <div style="display:flex;gap:6px;align-items:center"><i style="width:20px;height:20px;background:var(--deep)"></i><span style="flex:1;background:var(--blue);color:#fff;font-size:9px;font-weight:700;padding:4px 7px;letter-spacing:.6px">OUR MAJOR CLIENT'S</span></div>
      <div style="display:flex;gap:6px;align-items:center"><i style="width:20px;height:20px;background:var(--deep)"></i><span style="flex:1;background:var(--blue);color:#fff;font-size:9px;font-weight:700;padding:4px 7px;letter-spacing:.6px">OUR FACILITIES</span></div>
      <div style="display:flex;gap:6px;align-items:center"><i style="width:20px;height:20px;background:var(--deep)"></i><span style="flex:1;background:var(--blue);color:#fff;font-size:9px;font-weight:700;padding:4px 7px;letter-spacing:.6px">CERTIFICATIONS &amp; APPRECIATIONS</span></div>
    </div>
  </div>
</section>

<!-- Row 2 -->
<section class="slide col-l" style="top:400px">
  <div class="brand sm" style="right:auto;left:246px"><i></i>BRV</div>
  <div class="abs" style="left:0;top:52px;width:552px;height:224px;background:linear-gradient(90deg,var(--deep),var(--blue));border-radius:0 28px 28px 0"></div>
  <div class="ph" role="img" aria-label="Camera lens close-up" style="left:350px;top:72px;width:182px;height:68px;background:radial-gradient(circle at 50% 50%,#6f7a86,#1b2330 70%)"></div>
  <div class="abs white" style="left:440px;top:80px;font-size:34px;font-weight:700">V</div>
  <div class="ph" role="img" aria-label="Electronic test equipment rack" style="left:14px;top:130px;width:168px;height:68px;background:linear-gradient(90deg,#3a3f4a,#6b6f78)"></div>
  <div class="abs white" style="left:84px;top:138px;font-size:34px;font-weight:700">M</div>
  <div class="ph" role="img" aria-label="City skyline at night" style="left:334px;top:194px;width:182px;height:70px;background:linear-gradient(180deg,#0d1a33,#3a3a4a 60%,#a26a2a)"></div>
  <div class="abs white" style="left:410px;top:202px;font-size:34px;font-weight:700">G</div>
  <div class="abs white" style="left:64px;top:78px;width:270px"><div style="font-size:9px;font-weight:700">VISION</div><div style="font-size:7px;line-height:1.3">To become the leading solution provider in GCC for Industrial Electronic Services, Automation and Energy Efficiency Services</div></div>
  <div class="abs white" style="left:222px;top:148px;width:270px"><div style="font-size:9px;font-weight:700">MISSION</div><div style="font-size:7px;line-height:1.3">Develop new solutions to mitigate market challenges in Industrial Sector</div></div>
  <div class="abs white" style="left:34px;top:216px;width:285px"><div style="font-size:9px;font-weight:700">GOAL</div><div style="font-size:7px;line-height:1.3">Offer A One Stop Shop - cost effective solutions for all industrial sector in Controls, Automation and Energy Efficiency Field</div></div>
  <div class="pgno"></div>
</section>

<section class="slide col-r" style="top:400px">
  <div class="slide-title">OUR JOURNEY</div>
  <div class="brand sm"><i></i>BRV</div>
  <div class="ph" role="img" aria-label="Coastal city skyline with tower" style="left:0;top:50px;width:552px;height:96px;background:linear-gradient(180deg,#1aa7dc,#0b84c3 60%,#0c6fa8)"></div>
  <div class="abs white" style="left:128px;top:72px;width:300px;font-size:9px;font-weight:700;line-height:1.3">BRV is a Gulf Development Fund supported company, till date provided services to 30,000 Industrial electronic equipment's and supported 2,000 clients in Kuwait and Saudi.</div>
  <svg class="abs" style="left:0;top:150px" width="552" height="130" viewBox="0 0 552 130">
    <g font-family="Open Sans, sans-serif" font-size="7" fill="#1a2a3a">
      <rect x="80" y="42" width="410" height="16" fill="#0b5aa8"/>
      <g fill="#0692cd"><rect x="82" y="44" width="64" height="12"/><rect x="150" y="44" width="64" height="12"/><rect x="218" y="44" width="64" height="12"/><rect x="286" y="44" width="64" height="12"/><rect x="354" y="44" width="64" height="12"/><rect x="422" y="44" width="64" height="12"/></g>
      <g fill="#fff" font-weight="700" font-size="9" text-anchor="middle"><text x="114" y="54">2012</text><text x="182" y="54">2013</text><text x="250" y="54">2014</text><text x="318" y="54">2015</text><text x="386" y="54">2017</text><text x="454" y="54">2018</text></g>
      <g fill="#0692cd"><circle cx="72" cy="20" r="6"/><circle cx="218" cy="28" r="6"/><circle cx="356" cy="22" r="6"/><circle cx="152" cy="88" r="6"/><circle cx="282" cy="88" r="6"/><circle cx="424" cy="88" r="6"/></g>
      <g fill="#fff" font-size="7" font-weight="700" text-anchor="middle"><text x="72" y="23">1</text><text x="218" y="31">3</text><text x="356" y="25">5</text><text x="152" y="91">2</text><text x="282" y="91">4</text><text x="424" y="91">6</text></g>
      <text x="86" y="18">•Repairing Industrial</text><text x="88" y="26">Electronics</text><text x="86" y="38">•Field Maintenance - AMC</text>
      <text x="234" y="28">Riyadh (KSA)</text><text x="234" y="36">Established</text>
      <text x="370" y="16">Energy</text><text x="370" y="24">Monitoring</text><text x="370" y="32">Solutions</text>
      <text x="166" y="86">Automation</text><text x="166" y="94">Solutions</text>
      <text x="296" y="86">Dammam (KSA)</text><text x="296" y="94">Established</text>
      <g fill="#0692cd" font-weight="700" font-size="8"><text x="442" y="85">Smart</text><text x="442" y="95">Control</text><text x="442" y="105">Solutions</text></g>
    </g>
  </svg>
  <div class="pgno"></div>
</section>

<!-- Row 3 -->
<section class="slide col-l" style="top:734px">
  <div class="slide-title">OUR SERVICES</div>
  <div class="ph" role="img" aria-label="Technician repairing an electronic board at a test bench" style="left:330px;top:0;width:260px;height:310px;border-radius:160px 0 0 160px;background:linear-gradient(120deg,#8a96a3,#3d4856 60%,#222a35)"></div>
  <svg class="abs" style="left:0;top:0" width="552" height="310" viewBox="0 0 552 310">
    <circle cx="130" cy="156" r="54" fill="none" stroke="#0692cd" stroke-width="5"/>
    <path d="M160 44 Q280 156 160 268" fill="none" stroke="#d3dbe3" stroke-width="2"/>
    <g fill="#0692cd"><circle cx="169" cy="66" r="6"/><circle cx="190" cy="110" r="6"/><circle cx="196" cy="156" r="6"/><circle cx="190" cy="200" r="6"/><circle cx="169" cy="246" r="6"/></g>
    <g stroke="#d3dbe3" stroke-width="1.5"><line x1="175" y1="66" x2="250" y2="66"/><line x1="196" y1="110" x2="250" y2="110"/><line x1="202" y1="156" x2="250" y2="156"/><line x1="196" y1="200" x2="250" y2="200"/><line x1="175" y1="246" x2="250" y2="246"/></g>
  </svg>
  <div class="brand" style="left:94px;top:144px;font-size:20px"><i style="width:12px;height:12px"></i>BRV</div>
  <div class="abs" style="left:240px;top:50px;display:flex;flex-direction:column;gap:16px">
    <div style="display:flex;align-items:center;width:185px;height:30px;background:var(--blue);border-radius:15px;padding-left:4px;gap:6px"><i style="width:24px;height:24px;border-radius:50%;background:var(--deep);border:2px solid #fff"></i><span class="white" style="font-size:7.5px;font-weight:700;line-height:1.1">ENERGY EFFICIENCY<br>SERVICES</span></div>
    <div style="display:flex;align-items:center;width:185px;height:30px;background:var(--blue);border-radius:15px;padding-left:4px;gap:6px"><i style="width:24px;height:24px;border-radius:50%;background:var(--deep);border:2px solid #fff"></i><span class="white" style="font-size:7.5px;font-weight:700;line-height:1.1">INDUSTRIAL<br>AUTOMATION</span></div>
    <div style="display:flex;align-items:center;width:185px;height:30px;background:var(--blue);border-radius:15px;padding-left:4px;gap:6px"><i style="width:24px;height:24px;border-radius:50%;background:var(--deep);border:2px solid #fff"></i><span class="white" style="font-size:7.5px;font-weight:700;line-height:1.1">INDUSTRIAL ANNUAL<br>MAINTENANCE</span></div>
    <div style="display:flex;align-items:center;width:185px;height:30px;background:var(--blue);border-radius:15px;padding-left:4px;gap:6px"><i style="width:24px;height:24px;border-radius:50%;background:var(--deep);border:2px solid #fff"></i><span class="white" style="font-size:7.5px;font-weight:700;line-height:1.1">EMERGENCY<br>SERVICES</span></div>
    <div style="display:flex;align-items:center;width:185px;height:30px;background:var(--blue);border-radius:15px;padding-left:4px;gap:6px"><i style="width:24px;height:24px;border-radius:50%;background:var(--deep);border:2px solid #fff"></i><span class="white" style="font-size:7.5px;font-weight:700;line-height:1.1">INDUSTRIAL<br>REPAIR</span></div>
  </div>
  <div class="pgno"></div>
</section>

<section class="slide col-r" style="top:734px">
  <div class="slide-title">TEXT OPTIONS</div>
  <div class="brand sm"><i></i>BRV</div>
  <p class="abs" style="left:34px;top:64px;width:488px;font-size:9px;font-weight:700;line-height:1.35;color:#000">Lorem ipsum dolor sit amet, consectetur adipisicing elit, sed do eiusmod tempor incididunt ut labore et dolore magna aliqua. Ut enim ad minim veniam, quis nostrud exercitation ullamco laboris nisi ut aliquip ex ea commodo consequat.</p>
  <p class="abs" style="left:60px;top:122px;width:450px;font-size:7.5px;font-weight:600;line-height:1.35;color:#222">Lorem ipsum dolor sit amet, consectetur adipisicing elit, sed do eiusmod tempor incididunt ut labore et dolore magna aliqua. Ut enim ad minim veniam, quis nostrud exercitation ullamco laboris nisi ut aliquip ex ea commodo consequat.</p>
  <p class="abs lorem" style="left:94px;top:176px;width:430px">Lorem ipsum dolor sit amet, consectetur adipisicing elit, sed do eiusmod tempor incididunt ut labore et dolore magna aliqua. Ut enim ad minim veniam, quis nostrud exercitation ullamco laboris nisi ut aliquip ex ea commodo consequat.</p>
  <p class="abs lorem" style="left:150px;top:215px;width:250px">Lorem ipsum dolor sit amet, consectetur adipisicing elit, sed do eiusmod tempor incididunt ut labore et dolore magna aliqua. Duis aute irure dolor in reprehenderit in voluptate velit esse cillum dolore eu fugiat nulla pariatur. Excepteur sint occaecat cupidatat non proident.<br><br>Sed ut perspiciatis unde omnis iste natus error sit voluptatem accusantium doloremque laudantium, totam rem aperiam.</p>
  <div class="pgno"></div>
</section>

<!-- Row 4 -->
<section class="slide col-l" style="top:1069px">
  <div class="slide-title">PARAGRAPH OPTIONS</div>
  <div class="brand sm"><i></i>BRV</div>
  <p class="abs lorem" style="left:32px;top:76px;width:490px">Lorem ipsum dolor sit amet, consectetur adipisicing elit, sed do eiusmod tempor incididunt ut labore et dolore magna aliqua. Ut enim ad minim veniam, quis nostrud exercitation ullamco laboris nisi ut aliquip ex ea commodo consequat. Duis aute irure dolor in reprehenderit in voluptate velit esse cillum dolore eu fugiat nulla pariatur.</p>
  <p class="abs lorem" style="left:32px;top:110px;width:490px">Excepteur sint occaecat cupidatat non proident, sunt in culpa qui officia deserunt mollit anim id est laborum. Sed ut perspiciatis unde omnis iste natus error sit voluptatem accusantium doloremque laudantium, totam rem aperiam, eaque ipsa quae ab illo inventore veritatis et quasi architecto beatae vitae dicta sunt explicabo. Nemo enim ipsam voluptatem quia voluptas sit aspernatur aut odit aut fugit, sed quia consequuntur magni dolores eos qui ratione voluptatem sequi nesciunt.</p>
  <div class="abs" style="left:32px;top:180px;width:490px;display:flex;gap:20px">
    <div style="flex:1"><div class="sub">SUBTITLE GOES HERE</div><p class="lorem" style="margin-top:14px">Lorem ipsum dolor sit amet, consectetur adipisicing elit, sed do eiusmod tempor incididunt ut labore et dolore magna aliqua. Ut enim ad minim veniam, quis nostrud exercitation ullamco laboris nisi ut aliquip ex ea commodo consequat.</p></div>
    <div style="flex:1"><div class="sub">SUBTITLE GOES HERE</div><p class="lorem" style="margin-top:14px">Lorem ipsum dolor sit amet, consectetur adipisicing elit, sed do eiusmod tempor incididunt ut labore et dolore magna aliqua. Ut enim ad minim veniam, quis nostrud exercitation ullamco laboris nisi ut aliquip ex ea commodo consequat.</p></div>
    <div style="flex:1"><div class="sub">SUBTITLE GOES HERE</div><p class="lorem" style="margin-top:14px">Lorem ipsum dolor sit amet, consectetur adipisicing elit, sed do eiusmod tempor incididunt ut labore et dolore magna aliqua. Ut enim ad minim veniam, quis nostrud exercitation ullamco laboris nisi ut aliquip ex ea commodo consequat.</p></div>
  </div>
  <div class="pgno"></div>
</section>

<section class="slide col-r" style="top:1069px">
  <div class="slide-title">LIST SLIDE</div>
  <div class="brand sm"><i></i>BRV</div>
  <p class="abs lorem" style="left:68px;top:80px;width:420px">Excepteur sint occaecat cupidatat non proident, sunt in culpa qui officia deserunt mollit anim id est laborum. Sed ut perspiciatis unde omnis iste natus error sit voluptatem accusantium doloremque laudantium, totam rem aperiam, eaque ipsa quae ab illo inventore veritatis et quasi architecto beatae vitae dicta sunt explicabo.</p>
  <div class="abs" style="left:134px;top:132px;display:flex;flex-direction:column;gap:12px;font-size:6.5px;font-weight:700">
    <div style="display:flex;align-items:center;gap:8px"><span style="width:13px;height:13px;border-radius:50%;background:var(--deep);color:#fff;display:grid;place-items:center">1</span>Lorem ipsum dolor sit amet</div>
    <div style="display:flex;align-items:center;gap:8px"><span style="width:13px;height:13px;border-radius:50%;background:var(--blue);color:#fff;display:grid;place-items:center">2</span>Lorem ipsum dolor sit amet</div>
    <div style="display:flex;align-items:center;gap:8px"><span style="width:13px;height:13px;border-radius:50%;background:var(--deep);color:#fff;display:grid;place-items:center">3</span>Lorem ipsum dolor sit amet</div>
    <div style="display:flex;align-items:center;gap:8px"><span style="width:13px;height:13px;border-radius:50%;background:var(--blue);color:#fff;display:grid;place-items:center">4</span>Lorem ipsum dolor sit amet</div>
    <div style="display:flex;align-items:center;gap:8px"><span style="width:13px;height:13px;border-radius:50%;background:var(--deep);color:#fff;display:grid;place-items:center">5</span>Lorem ipsum dolor sit amet</div>
  </div>
  <div class="abs" style="left:330px;top:152px;width:88px;height:80px;background:linear-gradient(135deg,var(--blue),var(--deep));border-radius:0 22px 0 0"></div>
  <div class="pgno"></div>
</section>

<!-- Row 5 -->
<section class="slide col-l" style="top:1404px">
  <div class="slide-title">IMAGE + TEXT</div>
  <div class="brand sm"><i></i>BRV</div>
  <div class="abs" style="left:0;top:164px;width:552px;height:146px;background:linear-gradient(180deg,var(--blue),#0c83c4)"></div>
  <p class="abs lorem" style="left:74px;top:75px;width:410px">Excepteur sint occaecat cupidatat non proident, sunt in culpa qui officia deserunt mollit anim id est laborum. Sed ut perspiciatis unde omnis iste natus error sit voluptatem accusantium doloremque laudantium, totam rem aperiam, eaque ipsa quae ab illo inventore veritatis et quasi architecto beatae vitae dicta sunt explicabo.</p>
  <div class="ph" role="img" aria-label="Circuit board with capacitors" style="left:74px;top:134px;width:184px;height:104px;border:4px solid #fff;background:linear-gradient(135deg,#0f2a45,#2b5a7a)"></div>
  <div class="ph" role="img" aria-label="Hand testing an electronic control unit" style="left:290px;top:134px;width:186px;height:104px;border:4px solid #fff;background:linear-gradient(135deg,#d8dde3,#4d7aa8)"></div>
  <div class="pgno" style="border-color:#fff"></div>
</section>

<section class="slide col-r" style="top:1404px;background:linear-gradient(135deg,#0a84c8,var(--blue) 50%,#1aa3dd)">
  <div class="abs" role="img" aria-label="Soft blue network texture" style="left:0;top:0;width:552px;height:310px;background:radial-gradient(ellipse at 20% 40%,rgba(255,255,255,.12),rgba(255,255,255,0) 60%)"></div>
  <div class="abs white" style="left:0;right:0;top:146px;text-align:center;font-size:14px;font-weight:700;letter-spacing:2px;padding-left:40px">SECTION BREAK</div>
  <p class="abs white" style="left:82px;top:174px;width:400px;text-align:center;font-size:7px;line-height:1.35;letter-spacing:.3px">Excepteur sint occaecat cupidatat non proident, sunt in culpa qui officia deserunt mollit anim id est laborum. Sed ut perspiciatis unde omnis iste natus error sit voluptatem accusantium doloremque laudantium, totam rem aperiam, eaque</p>
</section>

<!-- Row 6 -->
<section class="slide col-l" style="top:1739px">
  <div class="ph" role="img" aria-label="Glowing blue digital horizon" style="left:0;top:0;width:552px;height:70px;background:radial-gradient(ellipse at 50% 10%,#8fdcff,#1a8ad0 35%,#0a2a55 80%);clip-path:path('M0 0 H552 V50 Q276 80 0 50 Z')"></div>
  <div class="ph" role="img" aria-label="Portrait of a team member" style="left:236px;top:42px;width:80px;height:80px;border-radius:50%;border:3px solid var(--blue);background:linear-gradient(180deg,#cfd6dd,#8796a6)"></div>
  <div class="abs sub" style="left:0;right:0;top:136px;text-align:center">SUBTITLE GOES HERE</div>
  <div class="abs" style="left:64px;top:164px;width:424px;display:flex;gap:8px">
    <p class="lorem" style="flex:1">Excepteur sint occaecat cupidatat non proident, sunt in culpa qui officia deserunt mollit anim id est laborum. Sed ut perspiciatis unde omnis iste natus error sit voluptatem accusantium doloremque laudantium, totam rem aperiam, eaque ipsa quae ab illo inventore veritatis et quasi architecto beatae vitae dicta sunt explicabo. Nemo enim ipsam voluptatem quia voluptas sit aspernatur.<br><br>Excepteur sint occaecat cupidatat non proident, sunt in culpa qui officia deserunt mollit anim id est laborum. Sed ut perspiciatis unde omnis iste natus error sit voluptatem accusantium doloremque laudantium, totam rem aperiam.</p>
    <p class="lorem" style="flex:1">Excepteur sint occaecat cupidatat non proident, sunt in culpa qui officia deserunt mollit anim id est laborum. Sed ut perspiciatis unde omnis iste natus error sit voluptatem accusantium doloremque laudantium, totam rem aperiam, eaque ipsa quae ab illo inventore veritatis et quasi architecto beatae vitae dicta sunt explicabo.<br><br>Excepteur sint occaecat cupidatat non proident, sunt in culpa qui officia deserunt mollit anim id est laborum. Nemo enim ipsam voluptatem quia voluptas sit aspernatur aut odit.</p>
  </div>
  <div class="pgno"></div>
</section>

<section class="slide col-r" style="top:1739px">
  <div class="slide-title">TITLE GOES HERE</div>
  <div class="brand sm"><i></i>BRV</div>
  <div class="abs" style="left:370px;top:100px;width:200px;height:230px;border-radius:50% 0 0 50%;background:linear-gradient(135deg,var(--blue),var(--deep))"></div>
  <div class="ph" role="img" aria-label="Colleagues talking in a bright office" style="left:284px;top:58px;width:154px;height:154px;border-radius:50%;background:linear-gradient(135deg,#eef1f4,#b9c2cb 60%,#6f7c89)"></div>
  <div class="abs" style="left:52px;top:94px;width:210px;font-size:7.5px;font-weight:600;font-style:italic;line-height:2.25;color:#333">“Lorem ipsum dolor sit amet, consectetur adipisicing elit, sed do eiusmod tempor incididunt ut labore et dolore magna aliqua. Ut enim ad minim veniam, quis nostrud exercitation ullamco laboris nisi commodo consequat.”<div style="color:var(--blue);font-style:normal;font-weight:700">– John Doe</div></div>
  <div class="pgno" style="border-color:#fff"></div>
</section>

<!-- Row 7 -->
<section class="slide col-l" style="top:2074px">
  <div class="slide-title">TABLE FORMAT</div>
  <div class="brand sm"><i></i>BRV</div>
  <table class="abs" style="left:98px;top:94px;width:360px;border-collapse:collapse;font-size:7px;text-align:center">
    <thead><tr style="background:var(--blue);color:#fff;font-weight:700"><th style="padding:6px 2px;background:var(--deep)">Subheading one</th><th>Subheading two</th><th>Subheading three</th><th>Subheading four</th></tr></thead>
    <tbody style="background:var(--panel);color:var(--grey)">
      <tr><td style="padding:5px 2px;font-weight:700;color:#222">Lorem ipsum du sit</td><td>Dolor</td><td>Dolor</td><td>Dolor</td></tr>
      <tr><td style="padding:5px 2px;font-weight:700;color:#222">Lorem ipsum du sit</td><td>Dolor</td><td>Dolor</td><td>Dolor</td></tr>
      <tr><td style="padding:5px 2px;font-weight:700;color:#222">Lorem ipsum du sit</td><td>Dolor</td><td>Dolor</td><td>Dolor</td></tr>
      <tr><td style="padding:5px 2px;font-weight:700;color:#222">Lorem ipsum du sit</td><td>Dolor</td><td>Dolor</td><td>Dolor</td></tr>
      <tr><td style="padding:5px 2px 12px;font-weight:700;color:#222">Lorem ipsum du sit</td><td style="padding-bottom:12px">Dolor</td><td style="padding-bottom:12px">Dolor</td><td style="padding-bottom:12px">Dolor</td></tr>
    </tbody>
  </table>
  <div class="pgno"></div>
</section>

<section class="slide col-r" style="top:2074px">
  <div class="brand" style="left:48px;top:62px;font-size:30px"><i style="width:24px;height:24px"></i>BRV</div>
  <div class="abs" style="left:84px;top:100px;font-size:7px;color:var(--blue)">A WORLD OF SOLUTIONS</div>
  <div class="abs" style="left:48px;top:124px;font-size:13px;font-weight:700;color:var(--deep)">IMAGES WITH TEXT</div>
  <p class="abs" style="left:48px;top:148px;width:250px;font-size:8px;line-height:1.4;color:#333">Lorem ipsum dolor sit amet, consectetur adipisicing elit, sed do eiusmod tempor incididunt ut labore et dolore magna aliqua. Ut enim ad minim veniam, quis nostrud exercitation ullamco laboris nisi ut aliquip ex ea commodo consequat. Duis aute irure dolor in reprehenderit in voluptate velit esse cillum dolore eu fugiat nulla pariatur. Excepteur sint occaecat cupidatat non proident, sunt in culpa qui officia deserunt mollit anim id est laborum.</p>
  <div class="ph" role="img" aria-label="Industrial robot arms in a factory" style="left:364px;top:0;width:84px;height:104px;background:linear-gradient(135deg,#e8ecef,#a74b3a)"></div>
  <div class="ph" role="img" aria-label="City at night" style="left:364px;top:108px;width:84px;height:202px;background:linear-gradient(180deg,#1b2540,#6a5a48)"></div>
  <div class="ph" role="img" aria-label="Close-up of a circuit board" style="left:452px;top:0;width:100px;height:310px;background:linear-gradient(180deg,#12324f,#2e6a8e 50%,#0f2236)"></div>
  <div class="pgno" style="border-color:#fff"></div>
</section>

<!-- Row 8 -->
<section class="slide col-l" style="top:2408px">
  <div class="slide-title">IMAGES WITH TEXT</div>
  <div class="brand sm"><i></i>BRV</div>
  <div class="abs" style="left:88px;top:74px;width:114px;height:96px;background:var(--blue);border-radius:0 0 0 26px"></div>
  <div class="ph" role="img" aria-label="Control room screens" style="left:98px;top:72px;width:104px;height:90px;border-radius:0 0 0 22px;background:linear-gradient(135deg,#2c3e52,#8aa3ba)"></div>
  <div class="abs" style="left:236px;top:96px;width:270px"><div class="sub">SUBTITLE GOES HERE</div><p class="lorem" style="margin-top:8px">Lorem ipsum dolor sit amet, consectetur adipisicing elit, sed do eiusmod tempor incididunt ut labore et dolore magna aliqua. Ut enim ad minim veniam, quis nostrud exercitation ullamco laboris nisi ut aliquip ex ea commodo consequat.</p></div>
  <div class="abs" style="left:104px;top:214px;width:230px"><div class="sub">SUBTITLE GOES HERE</div><p class="lorem" style="margin-top:8px">Lorem ipsum dolor sit amet, consectetur adipisicing elit, sed do eiusmod tempor incididunt ut labore et dolore magna aliqua. Ut enim ad minim veniam, quis nostrud exercitation ullamco laboris nisi ut aliquip ex ea commodo consequat.</p></div>
  <div class="abs" style="left:354px;top:192px;width:114px;height:104px;background:var(--blue);border-radius:0 0 26px 0"></div>
  <div class="ph" role="img" aria-label="Operators at monitoring workstations" style="left:354px;top:190px;width:104px;height:96px;border-radius:0 0 22px 0;background:linear-gradient(135deg,#1c2b3f,#b0455a 60%,#304a66)"></div>
  <div class="pgno"></div>
</section>

<section class="slide col-r" style="top:2408px">
  <div class="abs" style="left:0;right:0;top:38px;text-align:center;font-size:13px;font-weight:700;letter-spacing:1.5px;color:var(--deep)">TELL US HOW WE CAN <span style="color:var(--blue)">SUPPORT YOU!</span></div>
  <div class="abs" style="left:0;top:82px;width:552px;height:142px;background:linear-gradient(135deg,#0b7fc2,var(--blue))"></div>
  <div class="abs white" style="left:236px;top:100px">
    <div style="font-size:13px;font-weight:700;margin-bottom:8px">Contact Us</div>
    <div style="font-size:6.5px;line-height:16px">
      <div style="display:flex;gap:7px;align-items:center"><svg width="9" height="9" viewBox="0 0 10 10"><path d="M2 1 L4 1 L5 3 L4 4 Q5 6 6 6 L7 5 L9 6 L9 8 Q8 9 7 9 Q1 8 1 2 Q1 1 2 1Z" fill="#fff"/></svg>(123) 456 7880</div>
      <div style="display:flex;gap:7px;align-items:center"><svg width="9" height="9" viewBox="0 0 10 10"><circle cx="5" cy="5" r="4" fill="none" stroke="#fff"/><rect x="3" y="3.5" width="4" height="3" fill="#fff"/></svg>mail@website.com</div>
      <div style="display:flex;gap:7px;align-items:center"><svg width="9" height="9" viewBox="0 0 10 10"><circle cx="5" cy="5" r="4" fill="none" stroke="#fff"/><ellipse cx="5" cy="5" rx="1.8" ry="4" fill="none" stroke="#fff"/><line x1="1" y1="5" x2="9" y2="5" stroke="#fff"/></svg>www.brv-me.com</div>
      <div style="display:flex;gap:7px;align-items:center"><svg width="9" height="9" viewBox="0 0 10 10"><path d="M5 9 L2 5 A3 3 0 1 1 8 5 Z" fill="#fff"/><circle cx="5" cy="4" r="1.1" fill="#0692cd"/></svg>Street No., Location</div>
    </div>
  </div>
  <div class="brand" style="left:220px;top:250px;font-size:26px"><i style="width:22px;height:22px"></i>BRV</div>
  <div class="abs" style="left:256px;top:284px;font-size:6px;color:var(--blue)">A WORLD OF SOLUTIONS</div>
</section>

</body>
</html>
```